Long Term Insurance for Maturing Women

My business, is a Full service Life and Property Insurance Agency.. I want a reply card, Gloss, with woman showing Maturity, on a beach looking out at a Sun Set, with light Colors of Rainbow.
Thinking: If I am alone, how much income will I need to pay for a Long Term Sickness or Injury. ?
Do I have enough money set aside to cover the added expenses of a long Term Illness ?
Have I enough Life Insurance to cover final expenses, and leave my love ones free of any Debt from my Passing ?
These are real life's concerns, Please Call, let's start finding answers today !
Mark Dunstover, Agent # 0718294 at (714-555-3087) - Halvern Insurance & Financial Service LLC.
Markdun@halverninsx.com 4170 Tamsen Ave, Cypress Ca. 90512

Industry/Entity Type

Business

```html
<!DOCTYPE html>
<html lang="en">
<head>
<meta charset="utf-8">
<title>Long Term Insurance Reply Card</title>
<link rel="stylesheet" href="https://fonts.googleapis.com/css2?family=Varela+Round&family=Nunito:wght@500&family=Open+Sans:wght@400;700&display=swap">
<style>
  :root {
    --paper: #ffffff;
    --mark: #111111;
    --ink: #4a2a12;
    --ink-warm: #6b3416;
    --contact-ink: #3a2410;
    --sky-top: #d8b25c;
    --sky-glow: #f8e27a;
    --sun: #fff2a0;
    --horizon: #e9bf3c;
    --sea: #8c6418;
    --warm-left: #b07a3c;
    --band: rgba(250, 215, 140, 0.45);
    --frame: #3a2210;
  }
  * { margin: 0; padding: 0; box-sizing: border-box; }
  html, body { width: 1200px; height: 843px; overflow: hidden; background: var(--paper); }
  .sheet { position: relative; width: 1200px; height: 843px; }

  .crop-marks { position: absolute; inset: 0; }

  .card {
    position: absolute; left: 101px; top: 93px; width: 982px; height: 653px; overflow: hidden;
  }
  .card-photo {
    position: absolute; inset: 0;
    background:
      radial-gradient(ellipse 38% 30% at 58% 48%, var(--sun), transparent 70%),
      linear-gradient(90deg, var(--warm-left) 0%, rgba(176,122,60,0) 38%),
      linear-gradient(180deg, var(--sky-top) 0%, var(--sky-glow) 45%, var(--horizon) 76%, var(--sea) 100%);
  }
  .card-band {
    position: absolute; left: 0; top: 0; width: 272px; height: 100%;
    background: var(--band);
  }
  .card-lines { position: absolute; inset: 0; }

  .questions {
    position: absolute; right: 46px; top: 0;
    font-family: "Varela Round", sans-serif; font-size: 20px; color: var(--ink);
    text-align: right; letter-spacing: 0.3px;
  }
  .questions p { position: absolute; right: 0; white-space: nowrap; }

  .call-out {
    position: absolute; right: 46px;
    font-family: "Nunito", sans-serif; font-weight: 500; font-size: 23px; color: var(--ink-warm);
    text-align: right; white-space: nowrap;
  }

  .contact {
    position: absolute; right: 728px; top: 0;
    font-family: "Open Sans", sans-serif; font-size: 16px; color: var(--contact-ink);
    text-align: right; white-space: nowrap;
  }
  .contact p { position: absolute; right: 0; }
  .contact .agent-name { font-weight: 700; font-size: 16px; }
  .contact .agent-number { font-size: 12px; }
</style>
</head>
<body>
<div class="sheet">
  <svg class="crop-marks" width="1200" height="843" aria-hidden="true">
    <g stroke="var(--mark)" stroke-width="1.6">
      <line x1="132" y1="16" x2="132" y2="78"/>
      <line x1="1079" y1="16" x2="1079" y2="78"/>
      <line x1="132" y1="763" x2="132" y2="826"/>
      <line x1="1079" y1="763" x2="1079" y2="826"/>
      <line x1="33" y1="106" x2="95" y2="106"/>
      <line x1="1106" y1="106" x2="1168" y2="106"/>
      <line x1="33" y1="733" x2="95" y2="733"/>
      <line x1="1106" y1="733" x2="1168" y2="733"/>
    </g>
  </svg>

  <div class="card">
    <div class="card-photo" role="img" aria-label="Photo of a mature woman in a straw sun hat and sunglasses looking out over the sea at a golden sunset"></div>
    <div class="card-band"></div>

    <svg class="card-lines" width="982" height="653" aria-hidden="true">
      <g fill="none" stroke="var(--frame)" stroke-width="2.4">
        <rect x="332" y="42" width="620" height="188" rx="24"/>
        <rect x="332" y="230" width="620" height="186" rx="24"/>
        <rect x="49" y="339" width="217" height="296" rx="28"/>
        <line x1="202" y1="230" x2="332" y2="230"/>
      </g>
      <circle cx="202" cy="230" r="7" fill="var(--frame)"/>
      <circle cx="331" cy="163" r="8" fill="#ffffff" stroke="var(--frame)" stroke-width="2.4"/>
    </svg>

    <div class="questions">
      <p style="top:55px">Do I have enough savings?</p>
      <p style="top:94px">Will I have enough to cover any uncentities in the future?</p>
      <p style="top:133px">Do I have enough life insurance to cover&nbsp; all my</p>
      <p style="top:171px">expensives so as not to leave my love ones dept free?</p>
    </div>

    <p class="call-out" style="top:260px">These are real life's concerns,&nbsp;</p>
    <p class="call-out" style="top:295px">Please Call, let's start finding answers today</p>

    <div class="contact">
      <p class="agent-name" style="top:355px">Mark Dunstover</p>
      <p class="agent-number" style="top:377px">Agent # 0718294</p>
      <p style="top:411px">(714)-555-3087</p>
      <p style="top:454px">Halvern Insurance &amp;</p>
      <p style="top:476px">Financial Service LLC</p>
      <p style="top:520px">Markdun@halverninsx.com</p>
      <p style="top:563px">4170 Tamsen Ave</p>
      <p style="top:585px">Cypress Ca. 90512</p>
    </div>
  </div>
</div>
</body>
</html>
```